Create a Flyer for a Darts Tournament

We need a Flyer for a Darts Tournament that is going to be organized by our darts department (logo attached). The name of the tournament is "3. KLW Dartsturnier". The Flyer should look modern, professional and in a way that everyone can see at the first impression that is has to do with dart sports. The logo of our department should be on the flyer as well. On the flyer we need an area where we can place some informations regarding the tournament (bullet points) etc. And a area where we can place informations regarding the registration progress (e.g. "Registration via E-Mail". Should fit well to our logo.

Target Market(s)

Darts Players for the Tournament

Font styles to use
Serif

Colors

Designer to choose colors to be used in the design.

Requirements
Must have
• Name of the Tournament, our Logo, place for some tournament details, link to our registration page (besucher.tv-halmerau.de). Should

```html
<!DOCTYPE html>
<html lang="de">
<head>
<meta charset="utf-8">
<title>3. KLW Dartsturnier</title>
<link rel="stylesheet" href="https://fonts.googleapis.com/css2?family=Graduate&family=Saira+Condensed:wght@400;500;600;700&display=swap">
<style>
  :root {
    --page: #eef1f4;
    --navy: #0b2a4a;
    --deep: #08203b;
    --blue: #1a5a8e;
    --sky: #33b5ea;
    --ice: #8fd8f6;
    --white: #ffffff;
    --band: rgba(6, 26, 50, 0.55);
  }
  * { margin: 0; padding: 0; box-sizing: border-box; }
  html, body { width: 1200px; height: 2768px; overflow: hidden; background: var(--page); }
  .flyer {
    position: absolute; left: 120px; top: 764px;
    width: 960px; height: 1240px; overflow: hidden;
    background: var(--navy);
    font-family: "Saira Condensed", "Arial Narrow", sans-serif;
    color: var(--white); text-align: center;
  }
  .flyer-photo {
    position: absolute; inset: 0;
    background:
      radial-gradient(ellipse 70% 45% at 58% 48%, rgba(60,130,190,0.55), transparent 70%),
      radial-gradient(circle at 15% 10%, rgba(40,100,160,0.5), transparent 40%),
      linear-gradient(180deg, #123e68 0%, #0e3458 45%, #0a2747 100%);
  }
  .title-number {
    position: absolute; top: 56px; left: 0; right: 0;
    font-family: "Graduate", serif; font-size: 96px; line-height: 1;
    color: var(--sky); letter-spacing: 2px;
    text-shadow: 0 4px 0 var(--deep);
  }
  .title-main {
    position: absolute; top: 150px; left: 80px; right: 80px;
    font-family: "Graduate", serif; font-size: 84px; line-height: 1;
    color: var(--white); letter-spacing: 3px;
    -webkit-text-stroke: 3px var(--sky);
    paint-order: stroke fill;
    text-shadow: 0 5px 0 var(--deep);
  }
  .date {
    position: absolute; top: 236px; left: 0; right: 0;
    font-size: 64px; font-weight: 500; color: var(--ice); line-height: 1;
  }
  .time-bar {
    position: absolute; top: 312px; left: 170px; right: 170px; height: 58px;
    background: var(--sky); color: var(--deep);
    font-size: 38px; font-weight: 600; line-height: 58px;
  }
  .subtitle {
    position: absolute; top: 388px; left: 130px; right: 130px; height: 54px;
    background: var(--band);
    font-size: 36px; font-weight: 500; line-height: 54px;
  }
  .details {
    position: absolute; top: 500px; left: 170px; right: 170px;
    list-style: none; background: var(--band); padding: 14px 0;
  }
  .details li { font-size: 40px; font-weight: 600; line-height: 60px; }
  .club-mark {
    position: absolute; top: 840px; left: 0; right: 0;
    display: flex; flex-direction: column; align-items: center; gap: 14px;
  }
  .club-mark .dot {
    width: 120px; height: 120px; border-radius: 50%;
    background: var(--sky); border: 6px solid var(--white);
  }
  .club-mark .name {
    font-size: 64px; font-weight: 700; line-height: 1; color: var(--white); letter-spacing: 4px;
  }
  .contact {
    position: absolute; top: 1140px;
    font-size: 38px; font-weight: 500; line-height: 46px; color: var(--white);
  }
  .contact-info { left: 100px; width: 320px; }
  .contact-signup { right: 60px; width: 400px; }
</style>
</head>
<body>
  <main class="flyer">
    <div class="flyer-photo" role="img" aria-label="Foto einer Dartscheibe mit steckenden Dartpfeilen in Blautönen"></div>

    <h1>
      <span class="title-number">3. KLW</span>
      <span class="title-main">DARTSTURNIER</span>
    </h1>
    <p class="date">SAMSTAG, 25.01.2025</p>
    <p class="time-bar">Einlass 16:00 Uhr / Turnierbeginn 17:00 Uhr</p>
    <p class="subtitle">Steel-Darts-Hobbyturnier (keine Ligaspieler)</p>

    <ul class="details">
      <li>SVZ in 88471 Halmerau</li>
      <li>Maximal 48 Teilnehmer</li>
      <li>Gruppenphase 301 | DO | BO3</li>
      <li>KO-Phase 501 | DO | BO5</li>
    </ul>

    <div class="club-mark">
      <span class="dot"></span>
      <span class="name">KLW DARTS</span>
    </div>

    <p class="contact contact-info">Infos:<br>darts.tv-halmerau.de</p>
    <p class="contact contact-signup">Anmeldung:<br>besucher.tv-halmerau.de</p>
  </main>
</body>
</html>
```